Harlow Ridge Partners Business Cards

Design Business cards in a format where I can change the information and utilize a third party buisness card printing company

Contact Information for Business Card

Want Logo and Name on Back. Looking for Spot UV style shine on Logo. Probably Black background. Want smaller logo on front with contact details. Like rounded edges or something else interesting.

Requirements
Must have
• Strong masculine look.

```html
<!DOCTYPE html>
<html lang="en">
<head>
<meta charset="utf-8">
<title>Harlow Ridge Partners – Business Cards</title>
<link rel="stylesheet" href="https://fonts.googleapis.com/css2?family=Oswald:wght@500&family=Jost:wght@400;500&display=swap">
<style>
  :root {
    --bg: #2b2b2b;
    --card: #1e1e1e;
    --card-edge: #181818;
    --ink: #f2f2f2;
    --ink-soft: #d9d9d9;
    --gloss: #8a8a8a;
    --rule: #e6e6e6;
  }
  * { margin: 0; padding: 0; box-sizing: border-box; }
  html, body { width: 1200px; height: 899px; overflow: hidden; }
  body {
    background: var(--bg);
    display: flex;
    flex-direction: column;
    align-items: center;
    justify-content: center;
    gap: 40px;
    font-family: "Jost", sans-serif;
  }
  .card {
    width: 660px;
    height: 377px;
    background: var(--card);
    border: 1px solid var(--card-edge);
    border-radius: 18px;
    position: relative;
    overflow: hidden;
  }
  /* Back */
  .card-back {
    display: flex;
    align-items: center;
    justify-content: center;
    gap: 16px;
  }
  .brand-mark {
    width: 22px;
    height: 22px;
    background: var(--gloss);
    flex: none;
  }
  .brand-name {
    font-family: "Jost", sans-serif;
    font-weight: 500;
    color: var(--gloss);
    letter-spacing: 0.06em;
    text-transform: uppercase;
  }
  .card-back .brand-name { font-size: 30px; }
  /* Front */
  .card-front {
    display: grid;
    grid-template-columns: 300px 1px 1fr;
    align-items: center;
  }
  .front-brand {
    display: flex;
    flex-direction: column;
    align-items: center;
    gap: 14px;
    padding-left: 30px;
  }
  .front-brand .brand-mark { width: 18px; height: 18px; }
  .front-brand .brand-name { font-size: 20px; text-align: center; line-height: 1.25; }
  .divider {
    width: 1px;
    height: 220px;
    background: var(--rule);
  }
  .contact {
    padding-left: 40px;
    color: var(--ink-soft);
  }
  .person-name {
    font-family: "Oswald", sans-serif;
    font-weight: 500;
    font-size: 40px;
    letter-spacing: 0.02em;
    color: var(--ink);
    text-transform: uppercase;
    line-height: 1;
  }
  .person-role {
    font-size: 19px;
    font-weight: 500;
    color: var(--ink);
    margin-top: 4px;
  }
  .address {
    font-size: 18px;
    line-height: 1.3;
    margin-top: 18px;
    letter-spacing: 0.02em;
  }
  .contact-list { list-style: none; margin-top: 12px; }
  .contact-list li {
    display: flex;
    align-items: center;
    gap: 12px;
    font-size: 18px;
    line-height: 1.5;
    letter-spacing: 0.03em;
  }
  .contact-list svg { width: 18px; height: 18px; flex: none; }
</style>
</head>
<body>
  <section class="card card-back" aria-label="Card back">
    <span class="brand-mark"></span>
    <span class="brand-name">Harlow Ridge Partners</span>
  </section>

  <section class="card card-front" aria-label="Card front">
    <div class="front-brand">
      <span class="brand-mark"></span>
      <span class="brand-name">Harlow Ridge<br>Partners</span>
    </div>
    <div class="divider"></div>
    <div class="contact">
      <h1 class="person-name">Dorian Vale</h1>
      <p class="person-role">CEO &amp; Founder</p>
      <p class="address">Your Street Address Here,<br>New York City, 1234</p>
      <ul class="contact-list">
        <li>
          <svg viewBox="0 0 18 18" fill="none" stroke="#bdbdbd" stroke-width="1.5"><rect x="5" y="1.5" width="8" height="15" rx="1.5"/><line x1="8" y1="14" x2="10" y2="14"/></svg>
          000 111 2223
        </li>
        <li>
          <svg viewBox="0 0 18 18" fill="#bdbdbd"><path d="M1 4h16v10H1z"/><path d="M1 4l8 6 8-6" fill="none" stroke="#1e1e1e" stroke-width="1.4"/></svg>
          dvale@harlowridge.com
        </li>
        <li>
          <svg viewBox="0 0 18 18" fill="none" stroke="#bdbdbd" stroke-width="1.6"><circle cx="10.5" cy="7.5" r="5"/><line x1="7" y1="11" x2="2" y2="16"/></svg>
          www.harlowridge.com
        </li>
      </ul>
    </div>
  </section>
</body>
</html>
```